Business card design needed

Double sided
Color, unique, elegant

Maybe put this quote somewhere?? But I think it might make it to cluttered?
“The Pilates Method of Body
Conditioning develops the body
uniformly, corrects posture, restores
vitality, invigorates the mind and
elevates the spirit”
- Henrik Dovacombe

Industry/Entity Type

Business

Contact Information for Business Card

Marta Kellbrook
Pilates Instructor & Personal trainer
Mobile: 0498265043
www.lorvix.com.au
email: lorvixhealth.fitness@qentamail.com

```html
<!DOCTYPE html>
<html lang="en">
<head>
<meta charset="utf-8">
<title>Lorvix Health and Fitness — Business Card</title>
<link href="https://fonts.googleapis.com/css2?family=Open+Sans:wght@400;600&family=Dancing+Script:wght@500&display=swap" rel="stylesheet">
<style>
  :root {
    --backdrop: #2b2624;
    --card-white: #f6f6f4;
    --card-pink: #c974b4;
    --pink-deep: #9c4f8c;
    --pink-ink: #c23fa6;
    --pink-muted: #a45b97;
    --green: #6cc04a;
    --ink: #2e2e2e;
    --white: #ffffff;
    --stitch-light: #e0a9cf;
    --stitch-dark: #f0cbe4;
  }
  * { box-sizing: border-box; margin: 0; padding: 0; }
  html, body { width: 1200px; height: 823px; overflow: hidden; }
  body {
    background: var(--backdrop);
    position: relative;
    font-family: "Open Sans", Arial, sans-serif;
  }

  .card {
    position: absolute;
    top: 110px;
    width: 320px;
    height: 560px;
    border-radius: 26px;
    box-shadow: 0 18px 40px rgba(0,0,0,.45);
  }
  .card::before {
    content: "";
    position: absolute;
    inset: 10px;
    border-radius: 20px;
    border: 1.5px dashed var(--stitch-light);
  }
  .card--front { left: 330px; background: var(--card-white); }
  .card--back { left: 700px; background: var(--card-pink); }
  .card--back::before { border-color: var(--stitch-dark); }

  .brand { position: absolute; left: 0; right: 0; text-align: center; }
  .brand__name {
    font-family: "Open Sans", Arial, sans-serif;
    font-weight: 400;
    font-size: 36px;
    letter-spacing: 4px;
    line-height: 1;
  }
  .brand__tagline { font-family: "Open Sans", Arial, sans-serif; font-size: 15px; margin-top: 6px; }

  .card--front .brand { top: 130px; }
  .card--front .brand__name,
  .card--front .brand__tagline { color: var(--ink); }

  .quote {
    position: absolute;
    top: 270px;
    left: 36px;
    right: 36px;
    text-align: center;
    font-family: "Dancing Script", "Brush Script MT", cursive;
    font-weight: 500;
    color: var(--pink-ink);
    font-size: 21px;
    line-height: 1.3;
  }
  .quote__author {
    display: block;
    margin-top: 12px;
    font-family: "Open Sans", Arial, sans-serif;
    font-style: normal;
    font-weight: 600;
    font-size: 14px;
    color: var(--green);
  }

  .card--back .brand { top: 100px; }
  .card--back .brand__name,
  .card--back .brand__tagline { color: var(--pink-muted); }

  .name-bubble {
    position: absolute;
    top: 220px;
    left: 30px;
    right: 30px;
    height: 80px;
    background: var(--pink-deep);
    border-radius: 14px;
    padding: 14px 10px 0;
    text-align: center;
  }
  .name-bubble__tail {
    position: absolute;
    left: 20px;
    bottom: -34px;
    width: 40px;
    height: 36px;
  }
  .name-bubble__name {
    font-family: "Dancing Script", "Brush Script MT", cursive;
    font-weight: 500;
    font-size: 25px;
    color: var(--stitch-dark);
    line-height: 1.1;
    white-space: nowrap;
  }
  .name-bubble__role { font-size: 12px; color: var(--stitch-dark); margin-top: 6px; }

  .contacts {
    position: absolute;
    left: 34px;
    right: 20px;
    bottom: 44px;
    list-style: none;
  }
  .contacts__item {
    display: flex;
    align-items: center;
    gap: 10px;
    font-size: 12.5px;
    color: var(--pink-deep);
    margin-top: 10px;
  }
  .contacts__icon {
    width: 22px; height: 22px; flex: none;
    border-radius: 50%;
    background: var(--pink-deep);
    display: flex; align-items: center; justify-content: center;
  }

  .lockup {
    position: absolute;
    left: 70px;
    top: 630px;
    text-align: center;
    width: 200px;
  }
  .lockup .brand__name { color: var(--white); font-size: 38px; }
  .lockup .brand__tagline { color: var(--white); font-size: 17px; }
</style>
</head>
<body>

  <section class="card card--front">
    <div class="brand">
      <div class="brand__name">LORVIX</div>
      <div class="brand__tagline">Health and Fitness</div>
    </div>
    <blockquote class="quote">
      “ The Pilates Method of Body Conditioning develops the body uniformly, corrects posture, restores vitality, invigorates the mind and elevates the spirit ”
      <cite class="quote__author">Henrik Dovacombe</cite>
    </blockquote>
  </section>

  <section class="card card--back">
    <div class="brand">
      <div class="brand__name">LORVIX</div>
      <div class="brand__tagline">Health and Fitness</div>
    </div>
    <div class="name-bubble">
      <div class="name-bubble__name">Marta Kellbrook Pilates</div>
      <div class="name-bubble__role">Instructor &amp; Personal trainer</div>
      <svg class="name-bubble__tail" viewBox="0 0 40 36" aria-hidden="true">
        <path d="M0 0 H40 L4 36 Z" fill="#9c4f8c"/>
      </svg>
    </div>
    <ul class="contacts">
      <li class="contacts__item">
        <span class="contacts__icon">
          <svg width="12" height="12" viewBox="0 0 24 24" aria-hidden="true"><path fill="#f0cbe4" d="M6.6 10.8a15.1 15.1 0 0 0 6.6 6.6l2.2-2.2a1 1 0 0 1 1-.25 11.4 11.4 0 0 0 3.6.57 1 1 0 0 1 1 1V20a1 1 0 0 1-1 1A17 17 0 0 1 3 4a1 1 0 0 1 1-1h3.5a1 1 0 0 1 1 1c0 1.25.2 2.45.57 3.6a1 1 0 0 1-.25 1z"/></svg>
        </span>0498265043
      </li>
      <li class="contacts__item">
        <span class="contacts__icon">
          <svg width="12" height="12" viewBox="0 0 24 24" aria-hidden="true"><g fill="none" stroke="#f0cbe4" stroke-width="2"><circle cx="12" cy="12" r="9"/><path d="M3 12h18M12 3c3 3 3 15 0 18M12 3c-3 3-3 15 0 18"/></g></svg>
        </span>www.lorvix.com.au
      </li>
      <li class="contacts__item">
        <span class="contacts__icon">
          <svg width="12" height="12" viewBox="0 0 24 24" aria-hidden="true"><g fill="none" stroke="#f0cbe4" stroke-width="2"><rect x="3" y="5" width="18" height="14" rx="2"/><path d="M3 7l9 6 9-6"/></g></svg>
        </span>lorvixhealth.fitness@qentamail.com
      </li>
    </ul>
  </section>

  <div class="brand lockup">
    <div class="brand__name">LORVIX</div>
    <div class="brand__tagline">Health and Fitness</div>
  </div>

</body>
</html>
```